Kestra Health- Welcome

Under New Management / New Staff & New Physicians

Offering More Services

Accepting New Patients

Two Locations in the Bronx: North Bronx: 2915 Pellam Road – Office Phone: 718-555-0143
South Bronx: 564 Corvin Street – Office Phone: 718-555-0187

Our Services:
Primary Care
Gynecology
Cardiology
Dentistry
Psychology
Psychiatry
Neurology
Pain Management
Gastroenterology
Podiatry
Dermatology
Vascular Surgery
Physical Therapy
HIV / Infectious Disease

For an ZRPQ Mailing - we will drop off to Post Office

Front English
Back Smaller to have post office specs but have it in Spanish

```html
<!DOCTYPE html>
<html lang="en">
<head>
<meta charset="utf-8">
<title>Kestra Health – Welcome Mailer</title>
<link rel="stylesheet" href="https://fonts.googleapis.com/css2?family=Montserrat:wght@400;500;600;700;800&family=Roboto:wght@400;700;900&family=Roboto+Condensed:wght@400;500;700&display=swap">
<style>
  :root {
    --navy: #1c3782;
    --red: #c1121f;
    --grey-text: #8a8a8a;
    --ink: #262626;
    --sheet: #474747;
    --label: #f1f1f1;
    --panel: #f0f1f4;
    --white: #ffffff;
  }
  * { margin: 0; padding: 0; box-sizing: border-box; }
  html, body { width: 848px; height: 1200px; overflow: hidden; }
  body { background: var(--sheet); position: relative; font-family: "Roboto", Arial, sans-serif; }

  .card {
    position: absolute; left: 55px; width: 737px; height: 491px;
    background: var(--white); overflow: hidden;
    box-shadow: 0 2px 8px rgba(0,0,0,.35);
  }
  .card--front { top: 48px; }
  .card--back { top: 624px; }
  .abs { position: absolute; }

  .side-label {
    position: absolute; left: 0; width: 848px; text-align: center;
    font-family: "Montserrat", Arial, sans-serif; font-weight: 400;
    font-size: 21px; letter-spacing: 1.5px; color: var(--label);
  }

  /* Brand */
  .welcome {
    font-family: "Montserrat", Arial, sans-serif; font-weight: 700;
    color: var(--red); letter-spacing: 2.5px; white-space: nowrap;
  }
  .brand-name {
    font-family: "Montserrat", Arial, sans-serif; font-weight: 800;
    color: var(--navy); white-space: nowrap; letter-spacing: .5px;
  }
  .brand-tagline {
    font-family: "Montserrat", Arial, sans-serif; font-weight: 600;
    color: var(--navy); text-align: center; letter-spacing: 1.6px; white-space: nowrap;
    border-top: 1.5px solid var(--red); border-bottom: 1.5px solid var(--red);
  }

  /* Front header */
  .headline-new {
    right: 22px; text-align: right; color: var(--white);
    font-family: "Montserrat", Arial, sans-serif; font-weight: 800;
    font-size: 46px; line-height: 40px; letter-spacing: 2px; white-space: nowrap;
  }
  .headline-sub {
    left: 337px; right: 0; top: 97px; height: 27px; line-height: 27px;
    text-align: right; padding-right: 22px;
    color: var(--white); font-family: "Montserrat", Arial, sans-serif;
    font-weight: 700; font-size: 16px; letter-spacing: 3.3px; white-space: nowrap;
  }
  .slogan {
    left: 23px; top: 140px;
    font-family: "Roboto", Arial, sans-serif; font-weight: 900;
    font-size: 41px; line-height: 37px; color: var(--navy); white-space: nowrap;
  }
  .slogan .accent { color: var(--red); }
  .slogan-rule { left: 23px; top: 259px; width: 239px; height: 2px; background: var(--navy); }
  .offering {
    left: 23px; top: 271px; font-family: "Roboto Condensed", Arial, sans-serif;
    font-weight: 700; font-size: 24px; line-height: 22px; color: var(--grey-text);
  }
  .accepting {
    left: 20px; top: 321px; width: 232px; height: 87px;
    color: var(--white); font-family: "Roboto Condensed", Arial, sans-serif;
    font-weight: 700; font-size: 33px; line-height: 34px; text-align: center;
    padding: 9px 16px 0 0;
  }

  .photo-front {
    left: 300px; top: 124px; width: 437px; height: 236px;
    background:
      linear-gradient(180deg, rgba(255,255,255,0) 50%, #fff 100%),
      linear-gradient(90deg, #fff 0%, rgba(255,255,255,0) 18%),
      linear-gradient(90deg, #efe3dc 10%, #e8dcd6 25%, #aebfe4 45%, #8fa8da 58%, #c4cfe7 72%, #f1e4e6 88%, #f6f1f1 100%);
  }

  .services-tab {
    left: 289px; top: 314px; width: 27px; height: 103px; background: var(--navy);
    display: flex; align-items: center; justify-content: center;
  }
  .services-tab span {
    transform: rotate(-90deg); white-space: nowrap; color: var(--white);
    font-family: "Roboto Condensed", Arial, sans-serif; font-weight: 700;
    font-size: 15px; letter-spacing: .3px;
  }

  .service-list { list-style: none; position: absolute; font-family: "Roboto Condensed", Arial, sans-serif; font-weight: 500; color: var(--ink); white-space: nowrap; }
  .service-list li { position: relative; }
  .service-list .tick { position: absolute; left: 0; }
  .card--front .service-list { top: 311px; font-size: 15px; }
  .card--front .service-list li { line-height: 21.2px; padding-left: 22px; }
  .card--front .service-list .tick { top: 4.5px; width: 12px; height: 12px; }
  .card--front .service-list li.two-line { line-height: 17px; padding-top: 2px; }

  .card--back .service-list { top: 310px; font-size: 13px; }
  .card--back .service-list li { line-height: 20.3px; padding-left: 18px; }
  .card--back .service-list .tick { top: 4.5px; width: 11px; height: 11px; }
  .card--back .service-list li.two-line { line-height: 15px; padding-top: 2.5px; }
  .card--back .service-list li.two-line .tick { top: 4px; }

  /* Footer */
  .contact-bar { left: 0; bottom: 0; width: 737px; height: 67px; }
  .contact-bar svg { position: absolute; left: 0; top: 0; }
  .help-text { left: 16px; top: 8px; color: var(--white); font-family: "Roboto Condensed", Arial, sans-serif; white-space: nowrap; }
  .help-text .small { font-size: 12px; font-weight: 400; line-height: 13px; }
  .help-text .big { font-size: 18.5px; font-weight: 700; line-height: 19px; }
  .card--back .help-text .small { font-size: 11px; }
  .card--back .help-text .big { font-size: 16px; line-height: 19px; }
  .location { top: 15px; color: var(--white); white-space: nowrap; }
  .location .phone-icon { position: absolute; left: 0; top: 1px; width: 32px; height: 35px; }
  .location .number { position: absolute; left: 41px; top: 0; font-family: "Montserrat", Arial, sans-serif; font-weight: 700; font-size: 19px; line-height: 20px; letter-spacing: -.3px; }
  .location .address { position: absolute; left: 41px; top: 23px; font-family: "Montserrat", Arial, sans-serif; font-weight: 500; font-size: 11px; line-height: 13px; }
  .follow { left: 660px; top: 16px; width: 64px; text-align: center; color: var(--white); font-family: "Montserrat", Arial, sans-serif; font-size: 8.5px; font-weight: 500; }
  .follow-dot { position: absolute; top: 33px; width: 19px; height: 19px; border-radius: 50%; background: var(--red); }

  /* Back */
  .back-header {
    left: 0; top: 0; width: 392px; height: 95px; background: var(--red);
    color: var(--white); text-align: center; white-space: nowrap;
    font-family: "Montserrat", Arial, sans-serif; font-weight: 800;
    font-size: 26px; line-height: 31px; padding-top: 17px; letter-spacing: .3px;
  }
  .photo-back {
    left: 0; top: 95px; width: 392px; height: 178px;
    background:
      linear-gradient(90deg, rgba(210,225,240,.6) 0%, rgba(255,255,255,0) 30%),
      linear-gradient(100deg, #c9d6e6 0%, #eef1f6 25%, #e4e8ef 40%, #f4f5f8 55%, #3f64b3 75%, #2f56a6 90%, #dfe6ef 100%);
  }
  .back-panel { left: 0; top: 273px; width: 392px; height: 152px; background: var(--panel); border-top: 2px solid var(--navy); }
  .services-banner {
    left: 101px; top: 273px; width: 190px; height: 22px;
    clip-path: polygon(0 0, 100% 0, 95% 100%, 5% 100%);
    background: var(--navy); color: var(--white); text-align: center;
    font-family: "Roboto Condensed", Arial, sans-serif; font-weight: 700;
    font-size: 15.5px; line-height: 22px; letter-spacing: .4px;
  }
  .postage {
    left: 636px; top: 19px; width: 78px; height: 77px; border: 1px solid #777;
    font-family: Arial, Helvetica, sans-serif; font-size: 10px; line-height: 12.6px;
    color: #333; text-align: center; padding-top: 6px;
  }
</style>
</head>
<body>

<svg width="0" height="0" style="position:absolute">
  <defs>
    <symbol id="tick" viewBox="0 0 12 12">
      <circle cx="6" cy="6" r="5.1" fill="none" stroke="#c1121f" stroke-width="1.3"/>
      <path d="M3.6 6.1 L5.4 7.9 L8.6 4.4" fill="none" stroke="#c1121f" stroke-width="1.4" stroke-linecap="round" stroke-linejoin="round"/>
    </symbol>
    <symbol id="phone" viewBox="0 0 32 35">
      <rect x="9" y="1" width="17" height="31" rx="3" fill="none" stroke="#fff" stroke-width="2.4"/>
      <rect x="12.5" y="5.5" width="10" height="20" fill="#fff"/>
      <circle cx="17.5" cy="29" r="1.3" fill="#fff"/>
      <path d="M1 20 Q1 14 7 15 L11 17 L11 33 L5 33 Q1 29 1 20 Z" fill="#fff"/>
      <path d="M15 19 a3 3 0 0 1 3 -3 M15 16 a6 6 0 0 1 6 -6" fill="none" stroke="#1c3782" stroke-width="1.4"/>
    </symbol>
    <pattern id="scallop" width="13" height="7" patternUnits="userSpaceOnUse">
      <path d="M0 7 C2 0 11 0 13 7 Z" fill="#1c3782"/>
    </pattern>
    <linearGradient id="redFade" x1="0" y1="0" x2="1" y2="1">
      <stop offset="0" stop-color="#c8141f"/>
      <stop offset="1" stop-color="#8f0f19"/>
    </linearGradient>
  </defs>
</svg>

<!-- FRONT (English) -->
<section class="card card--front">
  <svg class="abs" style="left:0;top:0" width="737" height="130" aria-hidden="true">
    <polygon points="279,0 737,0 737,97 323,97" fill="#1c3782"/>
    <polygon points="323,97 737,97 737,124 337,124" fill="#c1121f"/>
  </svg>

  <div class="abs welcome" style="left:24px;top:30px;font-size:11px;line-height:13px;">WELCOME TO</div>
  <div class="abs brand-name" style="left:23px;top:47px;font-size:26px;line-height:32px;">KESTRA HEALTH</div>
  <div class="abs brand-tagline" style="left:23px;top:89px;width:231px;height:22px;font-size:10.5px;line-height:19px;">Better Care for a Better Life</div>

  <div class="abs headline-new" style="top:12px;">UNDER NEW</div>
  <div class="abs headline-new" style="top:52px;">MANAGEMENT</div>
  <div class="abs headline-sub">NEW STAFF &amp; NEW PHYSICIANS</div>

  <div class="abs slogan">BETTER<br>CARE FOR A<br><span class="accent">BETTER LIFE</span></div>
  <div class="abs slogan-rule"></div>
  <div class="abs offering">OFFERING MORE<br>SERVICES</div>

  <svg class="abs" style="left:0;top:315px" width="260" height="115" aria-hidden="true">
    <rect x="20" y="6" width="4" height="104" fill="#a5101b"/>
    <polygon points="20,6 220,6 249,50 220,93 20,93" fill="url(#redFade)"/>
  </svg>
  <div class="abs accepting">ACCEPTING<br>NEW PATIENTS</div>

  <div class="abs photo-front" role="img" aria-label="Photo of a smiling group of doctors and nurses in scrubs and white coats"></div>

  <div class="abs services-tab"><span>OUR SERVICES</span></div>

  <ul class="service-list" style="left:326px;">
    <li><svg class="tick"><use href="#tick"/></svg>Primary Care</li>
    <li><svg class="tick"><use href="#tick"/></svg>Gynecology</li>
    <li><svg class="tick"><use href="#tick"/></svg>Cardiology</li>
    <li><svg class="tick"><use href="#tick"/></svg>Dentistry</li>
    <li><svg class="tick"><use href="#tick"/></svg>Psychology</li>
  </ul>
  <ul class="service-list" style="left:448px;">
    <li><svg class="tick"><use href="#tick"/></svg>Psychiatry</li>
    <li><svg class="tick"><use href="#tick"/></svg>Neurology</li>
    <li><svg class="tick"><use href="#tick"/></svg>Pain Management</li>
    <li><svg class="tick"><use href="#tick"/></svg>Gastroenterology</li>
    <li><svg class="tick"><use href="#tick"/></svg>Podiatry</li>
  </ul>
  <ul class="service-list" style="left:594px;">
    <li><svg class="tick"><use href="#tick"/></svg>Dermatology</li>
    <li><svg class="tick"><use href="#tick"/></svg>Vascular Surgery</li>
    <li><svg class="tick"><use href="#tick"/></svg>Physical Therapy</li>
    <li class="two-line"><svg class="tick"><use href="#tick"/></svg>HIV / Infectious<br>Disease</li>
  </ul>

  <div class="abs contact-bar">
    <svg width="737" height="67" aria-hidden="true">
      <rect x="190" y="0" width="547" height="7" fill="url(#scallop)"/>
      <rect x="190" y="6.5" width="547" height="61" fill="#1c3782"/>
      <path d="M0 0 H194 Q204 0 208 9 L227 67 H0 Z" fill="url(#redFade)"/>
    </svg>
    <div class="abs help-text"><div class="small">WE ARE HERE TO HELP</div><div class="big">FOR MORE<br>DETAILS, CALL US</div></div>
    <div class="abs location" style="left:175px;">
      <svg class="phone-icon"><use href="#phone"/></svg>
      <div class="number">718-555-0143</div>
      <div class="address">North Bronx: 2915 Pellam Road</div>
    </div>
    <div class="abs location" style="left:399px;">
      <svg class="phone-icon"><use href="#phone"/></svg>
      <div class="number">718-555-0187</div>
      <div class="address">South Bronx: 564 Corvin Street</div>
    </div>
    <div class="abs follow">Follow Us</div>
    <div class="follow-dot" style="left:667px;"></div>
    <div class="follow-dot" style="left:691px;"></div>
  </div>
</section>

<div class="side-label" style="top:570px;">FRONT SIDE</div>

<!-- BACK (Spanish) -->
<section class="card card--back" lang="es">
  <div class="abs back-header">MEJOR ATENCIÓN PARA<br>UNA MEJOR VIDA</div>
  <div class="abs photo-back" role="img" aria-label="Foto de un médico con mascarilla escuchando el corazón de un paciente mayor con un estetoscopio"></div>
  <div class="abs back-panel"></div>
  <div class="abs services-banner">NUESTROS SERVICIOS</div>

  <ul class="service-list" style="left:14px;">
    <li><svg class="tick"><use href="#tick"/></svg>Atención Primaria</li>
    <li><svg class="tick"><use href="#tick"/></svg>Ginecología</li>
    <li><svg class="tick"><use href="#tick"/></svg>Cardiología</li>
    <li><svg class="tick"><use href="#tick"/></svg>Odontología</li>
    <li><svg class="tick"><use href="#tick"/></svg>Psicología</li>
  </ul>
  <ul class="service-list" style="left:138px;">
    <li><svg class="tick"><use href="#tick"/></svg>Psiquiatría</li>
    <li><svg class="tick"><use href="#tick"/></svg>Neurología</li>
    <li><svg class="tick"><use href="#tick"/></svg>Manejo del Dolor</li>
    <li><svg class="tick"><use href="#tick"/></svg>Gastroenterología</li>
    <li><svg class="tick"><use href="#tick"/></svg>Podiatría</li>
  </ul>
  <ul class="service-list" style="left:264px;">
    <li><svg class="tick"><use href="#tick"/></svg>Dermatología</li>
    <li><svg class="tick"><use href="#tick"/></svg>Cirugía Vascular</li>
    <li><svg class="tick"><use href="#tick"/></svg>Terapia Física</li>
    <li class="two-line"><svg class="tick"><use href="#tick"/></svg>VIH / Enfermedades<br>Infecciosas</li>
  </ul>

  <div class="abs welcome" style="left:428px;top:20px;font-size:8px;line-height:10px;letter-spacing:1.8px;">BIENVENIDOS A</div>
  <div class="abs brand-name" style="left:428px;top:32px;font-size:19px;line-height:22px;">KESTRA HEALTH</div>
  <div class="abs brand-tagline" style="left:428px;top:63px;width:150px;height:16px;font-size:6.4px;line-height:13px;letter-spacing:.7px;">Mejor atención para una mejor vida</div>

  <div class="abs postage" lang="en">PRSRT STD<br>ECRWSS<br>U.S. POSTAGE<br><b>PAID</b><br>ZRPQ RETAIL</div>

  <div class="abs contact-bar">
    <svg width="737" height="67" aria-hidden="true">
      <rect x="190" y="0" width="547" height="7" fill="url(#scallop)"/>
      <rect x="190" y="6.5" width="547" height="61" fill="#1c3782"/>
      <path d="M0 0 H194 Q204 0 208 9 L227 67 H0 Z" fill="url(#redFade)"/>
    </svg>
    <div class="abs help-text"><div class="small">ESTAMOS AQUÍ PARA AYUDARLE</div><div class="big">PARA MÁS<br>INFORMACIÓN, LLÁMENOS</div></div>
    <div class="abs location" style="left:190px;">
      <svg class="phone-icon"><use href="#phone"/></svg>
      <div class="number">718-555-0143</div>
      <div class="address">Bronx Norte: 2915 Pellam Road</div>
    </div>
    <div class="abs location" style="left:410px;">
      <svg class="phone-icon"><use href="#phone"/></svg>
      <div class="number">718-555-0187</div>
      <div class="address">Bronx Sur: 564 Corvin Street</div>
    </div>
    <div class="abs follow">Síganos</div>
    <div class="follow-dot" style="left:667px;"></div>
    <div class="follow-dot" style="left:691px;"></div>
  </div>
</section>

<div class="side-label" style="top:1142px;">BACK SIDE</div>

</body>
</html>
```